Design for web based travel expence program

We need a design template for a web based travel expence program we have created. The current design is based on a standard framework, and it needs to be "spiced" up.
Please notice that there are only 3-4 screen shots that needs an "upspice" of the design. No complete web design is expected for this price. For the right designer we have many more jobs coming up!
Velquor Accounting is a Scandinavian accounting company with offices in Norway (Oslo) and Stockholm (Sweden). Our goal is to be a proactive accounting company known for trouble-free solutions and wide knowledge about what we do. We have created an "easy" accounting program enabling clients to take picture of vouchers, upload them to our portal and gather them to a travel expense scheme that can be approved and sent directly into an accounting program.
The program is pure web based and created with sophisticated programming code, but only with a standard framework as design template. We need a touch of professional design that easily can be implemented “on top” of the framework.
We are thinking that the designer should add icons and create the squared elements a bit rounder and with a more beautiful touch.
We are looking for a designer that preferably can create CSS files with an improved design, though the first step should be to create some pictures/Photshop examples on how it could look like. The files we have uploaded are the screen shots that needs to be improved with a better design.
Target Market(s)
All type of businesses, but the end user is in focus. The program is designed to be easy-to-learn and very useful for all persons dealing with travel expence forms.
Industry/Entity Type
Accounting

```html
<!DOCTYPE html>
<html lang="no">
<head>
<meta charset="utf-8">
<title>Refusjoner – Velquor Accounting</title>
<link href="https://fonts.googleapis.com/css2?family=Lato:wght@400;700&display=swap" rel="stylesheet">
<style>
  :root {
    --page-bg: #c3d5de;
    --surface: #ffffff;
    --brand-dark: #1467ad;
    --brand-mid: #2f8fd3;
    --brand-light: #35a6dc;
    --brand-pale: #8ccbea;
    --nav-text: #1a6fae;
    --row-alt: #ebebeb;
    --row-line: #d6d6d6;
    --text: #4a4a4a;
    --muted: #9a9a9a;
    --footer-text: #3a9ad6;
  }
  * { box-sizing: border-box; margin: 0; padding: 0; }
  html, body { width: 1200px; height: 581px; overflow: hidden; }
  body {
    background: var(--page-bg);
    font-family: "Lato", Arial, sans-serif;
    color: var(--text);
    position: relative;
  }

  /* Sidebar */
  .sidebar {
    position: absolute; left: 12px; top: 12px;
    width: 139px; height: 555px;
    background: var(--surface);
    border-radius: 3px;
    overflow: hidden;
  }
  .sidebar-stripe { display: flex; height: 9px; }
  .sidebar-stripe span { flex: 1; }
  .sidebar-stripe span:nth-child(1) { background: var(--brand-dark); }
  .sidebar-stripe span:nth-child(2) { background: var(--brand-pale); }
  .sidebar-stripe span:nth-child(3) { background: var(--brand-light); }
  .sidebar-stripe span:nth-child(4) { background: var(--brand-mid); }
  .nav-item {
    display: flex; align-items: center; gap: 8px;
    height: 57px; padding-left: 18px;
    font-size: 9.5px; font-weight: 700; letter-spacing: .2px;
    color: var(--nav-text);
    box-shadow: 0 3px 4px -2px rgba(0,0,0,.12);
  }
  .nav-item + .nav-item { height: 55px; }
  .nav-icon { width: 16px; height: 16px; flex: none; }
  .nav-badge {
    background: var(--brand-mid); color: #fff;
    font-size: 8px; padding: 1px 3px; border-radius: 2px; margin-left: 2px;
  }

  /* Main panel */
  .main-panel {
    position: absolute; left: 164px; top: 13px;
    width: 1013px; height: 377px;
    background: var(--surface);
    border-radius: 4px;
  }
  .btn-new {
    position: absolute; left: 10px; top: 16px;
    width: 146px; height: 35px;
    background: linear-gradient(#2a83c9, var(--brand-dark));
    border-radius: 3px;
    color: #fff; font-size: 10px;
    display: flex; align-items: center; justify-content: space-between;
    padding: 0 10px 0 15px;
  }
  .search {
    position: absolute; left: 166px; top: 16px;
    width: 209px; height: 36px;
    border: 1px solid #dcdcdc; border-radius: 3px;
    display: flex; align-items: center; justify-content: space-between;
    padding: 0 8px 0 13px;
    font-size: 10px; color: #555;
  }

  .filter-list {
    position: absolute; left: 10px; top: 61px;
    width: 146px; height: 305px;
    background: var(--brand-light);
    border-radius: 3px;
    padding-top: 3px;
    list-style: none;
  }
  .filter-list li {
    display: flex; justify-content: space-between; align-items: center;
    height: 38px; padding: 0 14px 0 17px;
    color: #fff; font-size: 10px;
    box-shadow: 0 4px 5px -3px rgba(0,0,0,.12);
  }

  .refund-table {
    position: absolute; left: 167px; top: 61px;
    width: 824px;
    border-collapse: collapse;
    font-size: 9.5px;
  }
  .refund-table thead tr {
    background: linear-gradient(#3b9ee0, #2a7fc2);
    color: #fff;
  }
  .refund-table th {
    height: 35px; text-align: left; font-weight: 400; font-size: 11px;
  }
  .refund-table thead th:first-child { border-radius: 3px 0 0 3px; }
  .refund-table thead th:last-child { border-radius: 0 3px 3px 0; }
  .refund-table td {
    height: 38px; border-bottom: 1px solid var(--row-line);
  }
  .refund-table tbody tr:nth-child(even) { background: var(--row-alt); }
  .col-status { padding-left: 38px; width: 197px; }
  .col-title { width: 136px; }
  .col-receipts { width: 159px; }

  .footer-note {
    position: absolute; right: 27px; top: 559px;
    font-size: 8.5px; color: var(--footer-text);
  }
</style>
</head>
<body>
  <aside class="sidebar">
    <div class="sidebar-stripe"><span></span><span></span><span></span><span></span></div>
    <nav>
      <div class="nav-item">
        <svg class="nav-icon" viewBox="0 0 16 16" aria-hidden="true">
          <circle cx="8" cy="4" r="3" fill="#2f8fd3"/>
          <path d="M2 15c0-4 2.5-6 6-6s6 2 6 6z" fill="#2f8fd3"/>
          <path d="M5 11h6v2H5z" fill="#fff"/>
        </svg>
        REFUSJONER
      </div>
      <div class="nav-item">
        <svg class="nav-icon" viewBox="0 0 16 16" aria-hidden="true">
          <path d="M4 1l9 2-3 12-9-2z" fill="none" stroke="#2f8fd3" stroke-width="1.4"/>
          <path d="M5 5l5 1M4.5 7.5l5 1M4 10l4 1" stroke="#2f8fd3" stroke-width="1"/>
        </svg>
        KVITTERINGER <span class="nav-badge">3</span>
      </div>
    </nav>
  </aside>

  <main class="main-panel">
    <div class="btn-new">
      Ny Refusjon
      <svg width="18" height="18" viewBox="0 0 18 18" aria-hidden="true">
        <rect x="1.5" y="3.5" width="12" height="12" rx="1.5" fill="none" stroke="#fff" stroke-width="1.3"/>
        <path d="M7 11l1-3 7-7 2 2-7 7z" fill="#fff"/>
      </svg>
    </div>
    <div class="search">
      Sok
      <svg width="14" height="14" viewBox="0 0 14 14" aria-hidden="true">
        <circle cx="5.5" cy="5.5" r="4" fill="none" stroke="#c8c8c8" stroke-width="1.5"/>
        <path d="M8.5 8.5l4 4" stroke="#c8c8c8" stroke-width="2"/>
      </svg>
    </div>

    <ul class="filter-list">
      <li><span>Alle</span><span>[2]</span></li>
      <li><span>Lkke sendy</span><span>[2]</span></li>
      <li><span>Sendt</span><span>[0]</span></li>
      <li><span>Refundert</span><span>[0]</span></li>
    </ul>

    <table class="refund-table">
      <thead>
        <tr><th class="col-status">Status</th><th class="col-title">Tittel</th><th class="col-receipts">Kvitteringer</th><th>Belop</th></tr>
      </thead>
      <tbody>
        <tr><td class="col-status">Ikke sendt</td><td>Reise</td><td>Ukraina</td><td>3&nbsp; 3910.54</td></tr>
        <tr><td class="col-status">Ikke sendt</td><td>Utlegg</td><td>Juni</td><td>0&nbsp; 0</td></tr>
        <tr><td class="col-status">Ikke sendt</td><td>Reise</td><td>Ukraina</td><td>3&nbsp; 3910.54</td></tr>
        <tr><td class="col-status">Ikke sendt</td><td>Utlegg</td><td>Juni</td><td>0&nbsp; 0</td></tr>
      </tbody>
    </table>
  </main>

  <footer class="footer-note">Ver 0.1 © Velquor Accounting.</footer>
</body>
</html>
```